Free Printer Promotion

Hi i need a banner AD for my website.

The promotion is: free printer, for a monthly cost you get all the supplies and service included. Its a subscription service for printing. There is 5 plans available.
Prices vary upon printers, most expensive plan is $69.94 a month for a 1 year term and the most affordable plan is $9.95 a month for 3 year term

1 Monochrome laser (print only printer, black and white printing)
2 Multifunction Monochrome laser (print scan copy fax printer, black and white printing)

• Monochrome Printers are given 1000 prints per month
• Toner included
• Service included
• Printer included

3 Color laser (print only printer, color printing)
4 Multifunction Color laser (print scan copy fax, color printing)
Color printers are given 500 monochrome prints and 500 color prints per month
• Toner included
• Service included
• Printer included

5 Inkjet color printer (print copy scan fax, color printing)
• Inkjet Printers are given 1000 prints per month.
• Ink included
• Service included
• Printer included

Target Market(s)

students, home office workers, corporate business and government

Font styles to use
Serif
Sans Serif

Requirements
Must have
• i want it to be enticing, no long sentences. the customer will click on the banner and it will bring them to another page with the information.

Keep it short and sweet.

```html
<!DOCTYPE html>
<html lang="en">
<head>
<meta charset="utf-8">
<title>Free Printers – Banner Set</title>
<link href="https://fonts.googleapis.com/css2?family=Barlow+Condensed:wght@500&family=Montserrat:ital,wght@1,500;1,600;1,700&family=Poppins:wght@500;700&display=swap" rel="stylesheet">
<style>
  :root{
    --bg-top:#4fd1e1;
    --bg-bottom:#2b7db7;
    --card:#ffffff;
    --mint:#dcefeb;
    --brand-blue:#2a9de0;
    --ribbon-red:#ec1c24;
    --ink:#111111;
    --ink-soft:#333333;
    --label:#ffffff;
    --photo-a:#f4f4f4;
    --photo-b:#cfcfcf;
    --photo-top:#4a4a4a;
  }
  *{box-sizing:border-box;margin:0;padding:0}
  html,body{width:1152px;height:1200px;overflow:hidden}
  body{background:linear-gradient(160deg,var(--bg-top) 0%,#37a4dc 45%,var(--bg-bottom) 100%)}
  .board{position:absolute;left:0;top:0;width:868px;height:904px;transform:scale(1.3272);transform-origin:0 0}
  .size-label{position:absolute;font:500 11px/1 'Poppins',sans-serif;color:var(--label)}
  .banner{position:absolute;background:var(--card);overflow:hidden;box-shadow:4px 4px 7px rgba(0,0,0,.3)}
  .banner svg.deco{position:absolute;left:0;top:0}
  .abs{position:absolute}
  .price{font:500 28px/1 'Barlow Condensed',sans-serif;color:var(--ink)}
  .term{font:700 italic 11px/1.2 'Montserrat',sans-serif;color:var(--ink)}
  .headline{font:500 38px/1 'Barlow Condensed',sans-serif;color:var(--ink)}
  .headline .accent{color:var(--brand-blue)}
  .subline{font:600 italic 12.5px/1.2 'Montserrat',sans-serif;color:var(--ink-soft)}
  .cta{position:absolute;background:var(--ink);color:#fff;border-radius:999px;display:flex;align-items:center;justify-content:center;font:700 10px/1 'Poppins',sans-serif}
  .printer-photo{position:absolute;border-radius:4px;background:linear-gradient(180deg,var(--photo-top) 0 16%,var(--photo-a) 16%,var(--photo-b) 100%)}
  .ribbon-text{font-family:'Poppins',sans-serif;font-weight:700;fill:#fff}
  .features{position:absolute;list-style:none}
  .features li{display:flex;align-items:flex-start;gap:7px;font:700 italic 14px/1.1 'Montserrat',sans-serif;color:var(--ink);margin-bottom:7px}
  .features li small{display:block;font:700 italic 10px/1.3 'Montserrat',sans-serif}
  .features svg{flex:none;margin-top:2px}
</style>
</head>
<body>
<div class="board">

  <!-- Leaderboard 728x90 -->
  <span class="size-label" style="left:70px;top:69px">728×90</span>
  <section class="banner banner-leaderboard" style="left:70px;top:85px;width:728px;height:90px">
    <svg class="deco" width="728" height="90" viewBox="0 0 728 90">
      <path d="M0,90 L0,58 C110,22 250,18 380,48 C460,68 530,74 585,90 Z" fill="var(--mint)"/>
      <polygon points="0,42 62,0 88,0 0,62" fill="var(--ribbon-red)"/>
      <text class="ribbon-text" x="38" y="27" font-size="8.5" text-anchor="middle" dominant-baseline="central" transform="rotate(-35 38 27)">Affordable plan</text>
    </svg>
    <div class="abs price" style="left:95px;top:17px">$9.95</div>
    <div class="abs term" style="left:80px;top:48px;width:100px;text-align:center;font-size:10.5px">a month<br>for 3 year term</div>
    <div class="abs headline" style="left:213px;top:16px">
      <span class="accent">Free</span> Printers</div>
    <div class="abs subline" style="left:200px;top:58px">Multifunction Monochrome Laser</div>
    <div class="printer-photo" role="img" aria-label="Photo of a white multifunction monochrome laser printer" style="left:466px;top:12px;width:92px;height:58px"></div>
    <a class="cta" style="left:592px;top:30px;width:104px;height:29px">CLICK HERE</a>
  </section>

  <!-- Half page 300x600 -->
  <span class="size-label" style="left:70px;top:203px">300×600</span>
  <section class="banner banner-halfpage" style="left:70px;top:220px;width:300px;height:600px">
    <svg class="deco" width="300" height="600" viewBox="0 0 300 600">
      <path d="M0,80 C70,72 140,112 220,112 C260,112 285,108 300,104 L300,378 C220,398 150,440 0,432 Z" fill="var(--mint)"/>
      <polygon points="0,72 118,0 160,0 0,110" fill="var(--ribbon-red)"/>
      <text class="ribbon-text" x="68" y="47" font-size="14.5" text-anchor="middle" dominant-baseline="central" transform="rotate(-32 68 47)">Affordable plan</text>
    </svg>
    <div class="abs price" style="right:27px;top:24px;font-size:40px">$9.95</div>
    <div class="abs term" style="right:29px;top:64px;text-align:right;font-size:13.5px;line-height:1.35">a month<br>for 3 year term</div>
    <div class="abs headline" style="left:34px;top:150px;font-size:47px">
      <span class="accent">Free</span> Printers</div>
    <div class="abs subline" style="left:35px;top:202px;font-size:11.5px">Multifunction Monochrome Laser</div>
    <ul class="features" style="left:34px;top:239px">
      <li><svg width="12" height="10" viewBox="0 0 12 10"><polyline points="1,5 4.5,8.5 11,1" fill="none" stroke="var(--ink)" stroke-width="1.6"/></svg>
        <span>Monochrome Printers<small>1000 prints per month</small></span></li>
      <li><svg width="12" height="10" viewBox="0 0 12 10"><polyline points="1,5 4.5,8.5 11,1" fill="none" stroke="var(--ink)" stroke-width="1.6"/></svg>
        <span>Toner included</span></li>
      <li><svg width="12" height="10" viewBox="0 0 12 10"><polyline points="1,5 4.5,8.5 11,1" fill="none" stroke="var(--ink)" stroke-width="1.6"/></svg>
        <span>Service included</span></li>
      <li><svg width="12" height="10" viewBox="0 0 12 10"><polyline points="1,5 4.5,8.5 11,1" fill="none" stroke="var(--ink)" stroke-width="1.6"/></svg>
        <span>Printer included</span></li>
    </ul>
    <div class="printer-photo" role="img" aria-label="Photo of a white multifunction monochrome laser printer" style="left:53px;top:377px;width:194px;height:120px"></div>
    <a class="cta" style="left:72px;top:522px;width:156px;height:41px;font-size:13.5px">CLICK HERE</a>
  </section>

  <!-- Medium rectangle 300x250 -->
  <span class="size-label" style="left:414px;top:203px">300×250</span>
  <section class="banner banner-rectangle" style="left:414px;top:220px;width:300px;height:250px">
    <svg class="deco" width="300" height="250" viewBox="0 0 300 250">
      <path d="M0,0 H300 V76 C245,92 185,70 125,70 C75,70 40,86 0,78 Z" fill="var(--mint)"/>
      <polygon points="0,55 82,0 108,0 0,80" fill="var(--ribbon-red)"/>
      <text class="ribbon-text" x="47" y="34" font-size="10" text-anchor="middle" dominant-baseline="central" transform="rotate(-35 47 34)">Affordable plan</text>
    </svg>
    <div class="abs price" style="right:16px;top:10px;font-size:34px">$9.95</div>
    <div class="abs term" style="right:19px;top:46px;font-size:11.5px">a month for 3 year term</div>
    <div class="abs headline" style="left:21px;top:103px;font-size:35px;line-height:.95">
      <span class="accent">Free</span><br>Printers</div>
    <div class="abs subline" style="left:22px;top:177px;font-size:12.5px;line-height:1.35">Multifunction<br>Monochrome<br>Laser</div>
    <div class="printer-photo" role="img" aria-label="Photo of a white multifunction monochrome laser printer" style="left:153px;top:104px;width:130px;height:82px"></div>
    <a class="cta" style="left:178px;top:197px;width:104px;height:30px">CLICK HERE</a>
  </section>

  <!-- Skyscraper 120x240 -->
  <span class="size-label" style="left:414px;top:492px">120×24</span>
  <section class="banner banner-skyscraper" style="left:414px;top:508px;width:120px;height:240px">
    <svg class="deco" width="120" height="240" viewBox="0 0 120 240">
      <path d="M0,50 C40,40 80,66 120,60 V160 C80,170 40,150 0,156 Z" fill="var(--mint)"/>
      <polygon points="0,45 68,0 88,0 0,64" fill="var(--ribbon-red)"/>
      <text class="ribbon-text" x="39" y="27" font-size="7.5" text-anchor="middle" dominant-baseline="central" transform="rotate(-35 39 27)">Affordable plan</text>
    </svg>
    <div class="abs price" style="right:10px;top:18px;font-size:19px">$9.95</div>
    <div class="abs headline" style="left:0;top:55px;width:120px;text-align:center;font-size:23px;line-height:.95">
      <span class="accent">Free</span><br>Printers</div>
    <div class="abs subline" style="left:0;top:109px;width:120px;text-align:center;font-size:7.5px;line-height:1.4">Multifunction<br>Monochrome Laser</div>
    <div class="printer-photo" role="img" aria-label="Photo of a white multifunction monochrome laser printer" style="left:22px;top:142px;width:72px;height:45px"></div>
    <a class="cta" style="left:24px;top:202px;width:72px;height:20px;font-size:6.5px">CLICK HERE</a>
  </section>

</div>
</body>
</html>
```